Brackwell HVAC Service LLC Business Card

We just got a design created by one of your designers for a logo and now would like help with a business card design. The information to be included on the card is as follows:
Brackwell HVAC Service LLC (I will attach logo design)
P.O. Box 418
Halden, CO 80694
(970) 555-0147
Dale Vonnholt
I might include an e-mail address, but I'm not sure yet.
Target Market(s)
Customers needing service or repairs done on their heating and air conditioning systems.
Industry/Entity Type
Business
Contact Information for Business Card
P.O. Box 418
Halden, CO 80694
(970) 555-0147
Dale Vonnholt

```html
<!DOCTYPE html>
<html lang="en">
<head>
<meta charset="utf-8">
<title>Brackwell HVAC Service LLC – Business Card</title>
<link rel="stylesheet" href="https://fonts.googleapis.com/css2?family=Bebas+Neue&family=Jost:wght@400&display=swap">
<style>
  :root {
    --red-deep: #8e0d04;
    --red-bright: #d42608;
    --red-band: #3a0602;
    --white: #ffffff;
    --accent: #f6a21a;
    --mark: #b3160c;
  }
  * { margin: 0; padding: 0; box-sizing: border-box; }
  html, body { width: 1200px; height: 678px; overflow: hidden; background: #ffffff; }
  .card {
    position: relative;
    width: 1200px;
    height: 678px;
    overflow: hidden;
    background: var(--red-deep);
    font-family: "Bebas Neue", "Oswald", sans-serif;
    color: var(--white);
  }
  .panel-left {
    position: absolute; left: 0; top: 0; width: 585px; height: 663px;
    background: linear-gradient(160deg, #9a1005 0%, var(--red-deep) 60%, #7c0b03 100%);
  }
  .panel-right {
    position: absolute; left: 585px; top: 0; width: 615px; height: 663px;
    background: radial-gradient(ellipse at 20% 35%, var(--red-bright) 0%, #bd1c07 45%, #9a1205 100%);
  }
  .bottom-band {
    position: absolute; left: 0; bottom: 0; width: 100%; height: 15px;
    background: var(--red-band);
  }
  .flame-art {
    position: absolute; left: 110px; top: 110px; width: 440px; height: 553px;
    background: radial-gradient(ellipse at 50% 60%, rgba(200,40,20,0.35) 0%, rgba(160,20,10,0.15) 55%, rgba(0,0,0,0) 75%);
  }
  .brand {
    position: absolute; left: 30px; top: 38px;
    display: flex; align-items: center; gap: 14px;
  }
  .brand-dot {
    width: 62px; height: 62px; border-radius: 50%;
    background: var(--mark);
  }
  .brand-name {
    font-size: 34px; line-height: 1; letter-spacing: 1.5px; color: var(--white);
  }
  .address {
    position: absolute; left: 40px; top: 436px;
    font-size: 33px; line-height: 37px; letter-spacing: 3.5px;
  }
  .accent-marks {
    position: absolute; left: 1106px; top: 207px;
    display: flex; gap: 4px;
  }
  .accent-marks span { width: 15px; height: 20px; background: var(--accent); }
  .person-name {
    position: absolute; right: 57px; top: 246px;
    font-size: 50px; line-height: 1; letter-spacing: 1px; font-weight: 400;
  }
  .contact-row {
    position: absolute; left: 842px;
    display: flex; align-items: center;
    font-family: "Jost", "Futura", sans-serif;
  }
  .contact-phone { top: 304px; font-size: 29px; letter-spacing: 4.5px; }
  .contact-email { top: 359px; font-size: 19px; letter-spacing: 0.5px; }
  .contact-phone svg { width: 33px; height: 33px; margin-right: 20px; }
  .contact-email svg { width: 38px; height: 38px; margin-right: 16px; }
</style>
</head>
<body>
  <div class="card">
    <div class="panel-left"></div>
    <div class="panel-right"></div>
    <div class="flame-art" role="img" aria-label="Faint flame illustration"></div>
    <div class="bottom-band"></div>

    <div class="brand">
      <span class="brand-dot"></span>
      <span class="brand-name">Brackwell HVAC Service LLC</span>
    </div>

    <div class="address">
      <p>Brackwell HVAC Service LLC</p>
      <p>P.O. Box 418</p>
      <p>Halden, CO 80694</p>
    </div>

    <div class="accent-marks"><span></span><span></span></div>
    <h1 class="person-name">Dale Vonnholt</h1>

    <div class="contact-row contact-phone">
      <svg viewBox="0 0 32 32" aria-hidden="true">
        <rect x="1" y="1" width="30" height="30" rx="5" fill="#ffffff"/>
        <path d="M11 7c1 0 2 2.5 2.5 4 .3 1-1.5 2-1.5 2.5 0 1.5 3 5.5 5 6.5.6.3 1.6-1.6 2.6-1.3 1.4.5 3.9 1.8 3.9 2.8 0 1.5-2 3.5-4 3.5-5 0-11.5-7-11.5-12.5C8 9 10 7 11 7z" fill="#c81e0a"/>
      </svg>
      <span>(970) 555-0147</span>
    </div>

    <div class="contact-row contact-email">
      <svg viewBox="0 0 38 38" aria-hidden="true" fill="none" stroke="#ffffff" stroke-width="1.6">
        <circle cx="19" cy="19" r="17"/>
        <ellipse cx="19" cy="19" rx="8" ry="17"/>
        <line x1="19" y1="2" x2="19" y2="36"/>
        <line x1="2" y1="19" x2="36" y2="19"/>
        <path d="M5 10h28M5 28h28"/>
      </svg>
      <span>EMAIL ID</span>
    </div>
  </div>
</body>
</html>
```